Website Wordpress Design

Hello all,

Real Estate Investor seeking a sleek user friendly word-press website. We are using this site to promote our real estate deals and raising capital from individuals who want to learn how to make money in real estate. The site will have 5 pages, Below you will see files explaining the site format and logo design. The website address is quietharborledger.com.***Must be able to retrieve word-press log-in username and password for future updates***

Here are some sites we like: fenwickcapitalcircle.com and seniorcarebuildworks.com

Target Market(s)

Individuals 40 and above.

Industry/Entity Type

Real Estate

Contact Information for Business Card

I'm seeking a killer business card design see details below.
Tessa Morlow
Managing Partner
RTN Estates, LLC
482 Linwood Terrace Suite 356
Brooklyn, NY 11298
Direct:917-555-0143
www.quietharborledger.com
tessa@qhledger.com

Number of Pages Required

5+ page

Font styles to use
Serif
Sans Serif

Requirements
Must have
• Good Color schemes and appealing to the eye.
Should not have
• Money symbols or images of houses

```html
<!DOCTYPE html>
<html lang="en">
<head>
<meta charset="utf-8">
<title>Quiet Harbor Ledger</title>
<link href="https://fonts.googleapis.com/css2?family=Josefin+Sans:wght@400;600&family=Open+Sans:wght@400;600;700&display=swap" rel="stylesheet">
<style>
:root{
  --tan:#b5996a;
  --gold:#e2b266;
  --nav:#6e6966;
  --ink:#1b1b1b;
  --text:#444;
  --footer:#2b2b2b;
  --white:#fff;
  --card:#f3f3f3;
}
*{box-sizing:border-box;margin:0;padding:0}
html,body{width:1200px;height:2936px;overflow:hidden}
body{position:relative;background:var(--white);font-family:"Open Sans",Arial,sans-serif;color:var(--text)}
.abs{position:absolute}
.topbar{left:0;top:0;width:1200px;height:39px;background:var(--tan);color:var(--white);font-size:15px;font-weight:600}
.topbar .consult{left:62px;top:10px;display:flex;gap:8px;align-items:center}
.socials{right:42px;top:7px;display:flex;gap:6px}
.socials span{width:24px;height:24px;border-radius:50%;background:var(--white)}
.header{left:0;top:39px;width:1200px;height:82px}
.hours{left:60px;top:20px;display:flex;gap:10px;color:var(--ink)}
.hours b{font-size:17px;display:block}
.hours small{font-size:13px}
.callus{right:42px;top:22px;display:flex;gap:10px;color:var(--ink)}
.callus b{font-size:17px;display:block}
.callus small{font-size:13px}
.nav{left:0;top:121px;width:1200px;height:43px;background:var(--nav);font-size:15px;font-weight:600;color:var(--white)}
.nav a{position:absolute;top:12px;color:var(--white);text-decoration:none}
.nav a.active{border-bottom:3px solid var(--ink);padding-bottom:6px}
.logo{left:502px;top:0;width:174px;height:204px;background:var(--white);box-shadow:0 2px 8px rgba(0,0,0,.25);display:flex;flex-direction:column;align-items:center;justify-content:center;gap:10px;z-index:2}
.logo .mark{width:34px;height:34px;background:var(--tan)}
.logo .name{font-size:22px;font-weight:700;color:var(--tan);text-align:center;line-height:1.15}
.logo .tag{font-size:8px;font-weight:700;color:var(--ink);text-align:center;line-height:1.3}
.hero{left:0;top:164px;width:1200px;height:576px;background:linear-gradient(120deg,#9fb4bd 0%,#d9e2e6 35%,#c6c0b2 55%,#e6ecee 80%,#f4f6f7 100%)}
.hero-box{left:63px;top:376px;width:446px;height:195px;background:rgba(20,20,20,.82);padding:26px 20px}
.hero-box h1{font-size:28px;font-weight:700;color:var(--white);line-height:1.1}
.hero-box h2{font-size:17px;font-weight:700;color:var(--white);line-height:1.2;margin-top:4px}
.hero-btn{display:inline-block;margin-top:16px;background:var(--gold);color:var(--ink);font-weight:700;font-size:16px;padding:10px 12px}
.video{left:704px;top:319px;width:435px;height:295px;border:4px solid #3c3c3c;background:linear-gradient(180deg,#e3e6e8 0%,#cfc9c0 55%,#6a8f4a 78%,#3f6a2e 100%)}
.play{left:196px;top:116px}
.welcome{left:0;top:800px;width:1200px;text-align:center}
.welcome h2{font-family:"Josefin Sans",sans-serif;font-size:38px;font-weight:400;color:var(--ink)}
.welcome p{width:780px;margin:22px auto 0;font-size:12.5px;line-height:20px;color:#555}
.band{left:0;top:1239px;width:1200px;height:464px;background:var(--tan)}
.tiles{left:47px;top:994px;width:1104px;height:321px;display:flex}
.tile{flex:1;display:flex;flex-direction:column}
.tile .ph{height:262px}
.tile .lab{height:59px;display:flex;align-items:center;justify-content:center;font-family:"Josefin Sans",sans-serif;font-size:28px;color:var(--white)}
.query{left:62px;top:1392px;width:450px;color:var(--white)}
.query h3{font-family:"Josefin Sans",sans-serif;font-size:35px;font-weight:400;white-space:nowrap}
.query .p1{font-size:11px;line-height:17px;margin-top:12px;width:450px}
.query .p2{font-size:14px;line-height:21px;margin-top:10px}
.form{left:548px;top:1395px;width:594px;color:var(--white)}
.form h4{font-family:"Josefin Sans",sans-serif;font-size:26px;font-weight:400}
.field{position:absolute;background:var(--white);height:43px;font-size:12px;color:#888;padding:13px 10px}
.submit{position:absolute;background:#111;color:var(--white);font-size:16px;height:43px;width:138px;text-align:center;padding-top:11px}
.help{left:0;top:1703px;width:1200px;height:420px;background:linear-gradient(180deg,#c9cfd3 0%,#b9c0c3 55%,#a9aeae 100%)}
.help h2{position:absolute;top:58px;width:100%;text-align:center;font-family:"Josefin Sans",sans-serif;font-size:40px;font-weight:400;color:var(--ink)}
.service{position:absolute;top:150px;width:190px;text-align:center}
.service svg{display:block;margin:0 auto}
.service span{display:block;margin-top:20px;font-family:"Josefin Sans",sans-serif;font-size:27px;color:var(--ink)}
.blog h2{position:absolute;top:2164px;width:1200px;text-align:center;font-family:"Josefin Sans",sans-serif;font-size:40px;font-weight:400;color:var(--ink)}
.arrow{top:2365px}
.card{top:2274px;width:464px;height:231px;background:var(--card)}
.card .ph{position:absolute;left:0;top:0;width:218px;height:231px}
.card .body{position:absolute;left:232px;top:6px;width:222px}
.card h5{font-size:19px;font-weight:700;color:var(--ink)}
.card .meta{font-size:11px;color:#555;margin-top:8px;display:flex;gap:14px}
.card p{font-size:11px;line-height:19px;color:#666;margin-top:8px}
.card .more{display:inline-block;margin-top:10px;background:var(--tan);color:var(--white);font-size:12px;padding:8px 10px}
.footer{left:0;top:2584px;width:1200px;height:352px;background:var(--footer);color:#cfcfcf}
.footer h6{font-size:19px;font-weight:700;color:var(--white)}
.f-contact{position:absolute;left:48px;top:50px;width:380px}
.f-contact .intro{font-size:13px;line-height:22px;color:#9a9a9a;margin-top:30px}
.f-contact ul{list-style:none;margin-top:10px}
.f-contact li{font-size:13px;display:flex;gap:10px;align-items:center;height:32px;color:#bbb}
.f-explore{position:absolute;left:480px;top:52px;width:280px}
.f-explore ul{list-style:none;position:absolute;top:54px;font-size:12.5px;color:var(--white)}
.f-explore li{height:33px}
.f-sub{position:absolute;left:818px;top:52px;width:336px}
.f-sub .line{height:1px;background:#4a4a4a;margin-top:14px}
.f-sub .box{margin-top:26px;display:flex;height:40px}
.f-sub .box .in{flex:1;background:var(--white)}
.f-sub .box .btn{width:64px;background:var(--gold);display:flex;align-items:center;justify-content:center}
.f-sub .note{font-size:13px;color:#999;margin-top:14px}
.f-sub .links{display:grid;grid-template-columns:136px 140px;row-gap:18px;margin-top:42px;font-size:12.5px;color:var(--white)}
.copy{position:absolute;left:0;width:1200px;border-top:1px solid #444;text-align:center;font-size:12px;color:#ddd;padding-top:12px}
</style>
</head>
<body>

<div class="abs topbar">
  <div class="abs consult">
    <svg width="14" height="14" viewBox="0 0 14 14"><circle cx="7" cy="4" r="3.2" fill="#fff"/><path d="M1 14c0-4 3-6 6-6s6 2 6 6z" fill="#fff"/></svg>
    Consulting with us
  </div>
  <div class="abs socials"><span></span><span></span><span></span><span></span></div>
</div>

<div class="abs header">
  <div class="abs hours">
    <svg width="24" height="24" viewBox="0 0 24 24"><circle cx="12" cy="12" r="10" fill="none" stroke="#1b1b1b" stroke-width="2.4"/><path d="M12 6v6l4 3" fill="none" stroke="#1b1b1b" stroke-width="2.4"/></svg>
    <div><b>Opening Houres</b><small>Monday to friday | 8:30am to 5:30pm</small></div>
  </div>
  <div class="abs callus">
    <svg width="14" height="26" viewBox="0 0 14 26"><path d="M4 2c-3 2-3 6-1 12s4 9 8 10l2-4-4-3-2 2c-1-1-2-4-3-7l3-1-1-5z" fill="#1b1b1b"/></svg>
    <div><b>Call us on</b><small>+555 201 7734, 555 2019</small></div>
  </div>
</div>

<nav class="abs nav">
  <a class="active" style="left:58px">HOME</a>
  <a style="left:143px">ABOUT US</a>
  <a style="left:263px">REAL ESTATE</a>
  <a style="left:390px">SHOWS</a>
  <a style="left:714px">VIDEO</a>
  <a style="left:798px">BLOGS</a>
  <a style="left:891px">VENDORS</a>
  <a style="left:1007px">CONTACT US</a>
</nav>

<div class="abs logo">
  <div class="mark"></div>
  <div class="name">QUIET HARBOR<br>LEDGER</div>
  <div class="tag">STEADY GROUND FOR<br>PATIENT INVESTORS</div>
</div>

<section class="abs hero" role="img" aria-label="Photo of a model building on a desk beside hands signing papers"></section>
<div class="abs hero-box">
  <h1>A PLAIN GUIDE TO</h1>
  <h2>BUILDING STEADY RENTAL INCOME FOR THE LONG TERM</h2>
  <span class="hero-btn">GET YOUR FREE GUIDE NOW</span>
</div>
<div class="abs video" role="img" aria-label="Video still of a family relaxing on a lawn outdoors">
  <svg class="abs play" width="76" height="76" viewBox="0 0 76 76"><circle cx="38" cy="38" r="37" fill="#d21414"/><path d="M29 22l26 16-26 16z" fill="#fff"/></svg>
</div>

<section class="abs welcome">
  <h2>WELCOME TO QUIET HARBOR LEDGER</h2>
  <p>Behind the word mountains, far from the countries Vokalia and Consonantia, there live the blind texts. Separated they live in Bookmarks grove right at the coast of the Semantics, a large language ocean.Far far away, behind the word mountains, far from the countries there live the blind texts.</p>
</section>

<div class="abs band"></div>
<div class="abs tiles">
  <div class="tile"><div class="ph" role="img" aria-label="Photo of hands using a tablet at a wooden desk" style="background:linear-gradient(135deg,#5a4a3c,#9a8a78)"></div><div class="lab" style="background:#0d0d0d">HIRE US</div></div>
  <div class="tile"><div class="ph" role="img" aria-label="Photo of a couple planning a renovation" style="background:linear-gradient(135deg,#d9cfc2,#f2efea)"></div><div class="lab" style="background:#3f3f3f">WORKING WITH US</div></div>
  <div class="tile"><div class="ph" role="img" aria-label="Photo of keys being handed over across a desk" style="background:linear-gradient(135deg,#e9e6e2,#b94a45 60%,#dedad6)"></div><div class="lab" style="background:#8c8c8c">SUCCEED!</div></div>
</div>

<div class="abs query">
  <h3>MAIL US &amp; ASK A QUERY</h3>
  <p class="p1">simply dummy text of the printing and typesetting industry. Lorem Ipsum has been the industry's standard dummy text</p>
  <p class="p2">simply dummy text of the printing and typesetting industry. Lorem Ipsum has been the industry's standard dummy text.simply dummy text of the printing and typesetting industry. Lorem Ipsum has been the industry's standard dummy text</p>
</div>
<div class="abs form">
  <h4>Please Fill Your Information</h4>
  <div class="field" style="left:0;top:78px;width:297px">Your Name</div>
  <div class="field" style="left:314px;top:78px;width:280px">Email Here</div>
  <div class="field" style="left:0;top:143px;width:299px">Your Message</div>
  <div class="submit" style="left:317px;top:143px">Submit</div>
</div>

<section class="abs help" role="img" aria-label="Faded photo of a city skyline with tall towers">
  <h2>HOW WE CAN HELP YOU</h2>
  <div class="service" style="left:45px">
    <svg width="150" height="150" viewBox="0 0 150 150"><circle cx="75" cy="75" r="72" fill="var(--gold)" stroke="#111" stroke-width="5"/><path d="M52 52v46h48" fill="none" stroke="#111" stroke-width="4"/><rect x="60" y="80" width="7" height="14" fill="#111"/><rect x="71" y="70" width="7" height="24" fill="#111"/><rect x="82" y="76" width="7" height="18" fill="#111"/><path d="M58 72l14-12 10 8 14-14" fill="none" stroke="#111" stroke-width="3"/></svg>
    <span>Marketing</span>
  </div>
  <div class="service" style="left:270px">
    <svg width="150" height="150" viewBox="0 0 150 150"><circle cx="75" cy="75" r="72" fill="var(--gold)" stroke="#111" stroke-width="5"/><rect x="49" y="53" width="52" height="36" fill="none" stroke="#111" stroke-width="4"/><path d="M68 89l-4 10h22l-4-10" fill="#111"/><rect x="57" y="70" width="6" height="12" fill="#111"/><rect x="67" y="64" width="6" height="18" fill="#111"/><circle cx="86" cy="71" r="8" fill="#111"/></svg>
    <span>Feasibility</span>
  </div>
  <div class="service" style="left:513px">
    <svg width="150" height="150" viewBox="0 0 150 150"><circle cx="75" cy="75" r="72" fill="var(--gold)" stroke="#111" stroke-width="5"/><rect x="56" y="48" width="38" height="54" rx="3" fill="none" stroke="#111" stroke-width="4"/><path d="M63 62h24M63 71h24M63 80h24M63 89h16" stroke="#111" stroke-width="3"/></svg>
    <span>Training</span>
  </div>
  <div class="service" style="left:737px">
    <svg width="150" height="150" viewBox="0 0 150 150"><circle cx="75" cy="75" r="72" fill="#111" stroke="var(--gold)" stroke-width="5"/><circle cx="58" cy="64" r="8" fill="var(--gold)"/><path d="M44 92c0-10 6-16 14-16s14 6 14 16z" fill="var(--gold)"/><path d="M78 62h28M78 72h28M78 82h28" stroke="var(--gold)" stroke-width="4"/></svg>
    <span>Consulting</span>
  </div>
  <div class="service" style="left:965px">
    <svg width="150" height="150" viewBox="0 0 150 150"><circle cx="75" cy="75" r="72" fill="var(--gold)" stroke="#111" stroke-width="5"/><circle cx="75" cy="75" r="26" fill="none" stroke="#111" stroke-width="4" stroke-dasharray="14 6"/><circle cx="75" cy="75" r="7" fill="#111"/><circle cx="75" cy="56" r="4" fill="#111"/><circle cx="92" cy="84" r="4" fill="#111"/><circle cx="58" cy="84" r="4" fill="#111"/></svg>
    <span>Development</span>
  </div>
</section>

<section class="blog">
  <h2>FROM OUR BLOG</h2>
  <svg class="abs arrow" style="left:62px" width="24" height="44" viewBox="0 0 24 44"><path d="M20 4L4 22l16 18" fill="none" stroke="#333" stroke-width="4"/></svg>
  <svg class="abs arrow" style="left:1114px" width="24" height="44" viewBox="0 0 24 44"><path d="M4 4l16 18L4 40" fill="none" stroke="#333" stroke-width="4"/></svg>
  <article class="abs card" style="left:123px">
    <div class="ph" role="img" aria-label="Photo of a model building on a wooden surface" style="background:linear-gradient(160deg,#f3f1ee,#a47a56 65%,#7d8a66)"></div>
    <div class="body">
      <h5>Beciegast nveriti vitaes</h5>
      <div class="meta"><span>27 May,16</span><span>2:00 pm</span></div>
      <p>Beciegast nveriti vitaesaert asety kertya aserdenerafae kertyuraue styasnemo faseriasera labore et dolore magnam liaseras.Beciegast nveriti vitaesaert asety kertya</p>
      <span class="more">Read More</span>
    </div>
  </article>
  <article class="abs card" style="left:607px">
    <div class="ph" role="img" aria-label="Photo of a small red model building" style="background:linear-gradient(160deg,#e8edf1,#c9a25a 60%,#b4873f)"></div>
    <div class="body">
      <h5>Beciegast nveriti vitaes</h5>
      <div class="meta"><span>27 May,16</span><span>2:00 pm</span></div>
      <p>Beciegast nveriti vitaesaert asety kertya aserdenerafae kertyuraue styasnemo faseriasera labore et dolore magnam liaseras.Beciegast nveriti vitaesaert asety kertya</p>
      <span class="more">Read More</span>
    </div>
  </article>
</section>

<footer class="abs footer">
  <div class="f-contact">
    <h6>Contact Us</h6>
    <p class="intro">Harbor Finance is one of the world's Leading financial consulting films.</p>
    <ul>
      <li><svg width="10" height="14" viewBox="0 0 10 14"><path d="M5 0a5 5 0 015 5c0 4-5 9-5 9S0 9 0 5a5 5 0 015-5z" fill="#bbb"/><circle cx="5" cy="5" r="2" fill="#2b2b2b"/></svg>14 Alder Row, Millbeck, Kellstown, Eirmoor, K7Q 2LM.</li>
      <li><svg width="10" height="14" viewBox="0 0 10 14"><path d="M2 1C0 3 1 8 4 11s5 3 6 2l-2-3-2 1C5 10 4 8 3 6l2-1-1-4z" fill="#bbb"/></svg>00555-21-7730142</li>
      <li><svg width="14" height="10" viewBox="0 0 14 10"><rect width="14" height="10" fill="#bbb"/><path d="M0 0l7 6 7-6" fill="none" stroke="#2b2b2b"/></svg>rwalsh@ledgerline-mail.com</li>
      <li><svg width="14" height="12" viewBox="0 0 14 12"><rect x="1" y="1" width="12" height="8" fill="none" stroke="#bbb" stroke-width="1.5"/><path d="M4 11h6" stroke="#bbb" stroke-width="1.5"/></svg>www.ledgerline-mail.com</li>
    </ul>
  </div>
  <div class="f-explore">
    <h6>Explore</h6>
    <ul style="left:2px"><li>Home</li><li>Service</li><li>News</li><li>Bonds</li><li>Investments</li><li>Stocks</li></ul>
    <ul style="left:133px"><li>About Us</li><li>Testimonials</li><li>Contact Us</li><li>Commodities</li><li>Retirement</li><li>Trends</li></ul>
  </div>
  <div class="f-sub">
    <h6>Subscribe</h6>
    <div class="line"></div>
    <div class="box"><div class="in"></div><div class="btn"><svg width="20" height="14" viewBox="0 0 20 14"><rect width="20" height="14" fill="#fff"/><path d="M0 0l10 8 10-8" fill="none" stroke="#e2b266" stroke-width="1.5"/></svg></div></div>
    <p class="note">Get Latest updates and offers.</p>
    <div class="links"><span>Friendwall</span><span>Circle Plus</span><span>Chirper</span><span>Linkwork</span></div>
  </div>
  <div class="copy" style="top:309px">© 2016 Quiet Harbor Ledger Right Reserved.</div>
</footer>

</body>
</html>
```